Flyer für dynamisches Maklerteam
The design process with Brightwing went very well. He responded precisely to our requirements and to our target group and developed designs that reflect our logo and our corporate identity in many small details. Communication with Brightwing went great. He quickly translated our requests into wonderful designs and created flyers that we are very happy with. Brightwing is a good designer and I can highly recommend working with him. Dr. Ilse Brandvoort KORVEN Real Estate
Zielgruppe
KORVEN Immobilien ist ein dynamisches Maklerteam, dass sich auf den Verkauf von Wohnimmobilien des gehobenen Preissegmentes spezialisiert hat. Unser Schwerpunkt liegt auf Luxusobjekten.
Hallo,
schön, dass ihr an unserem Design-Wettbewerb teilnehmt.
Unser Zielgruppe sind verkaufswillige Eigentümer hochpreisiger Immobilien.
--> eine ganz wichtige Kundengruppe sind Erben, die ihre geerbte Immobilie verkaufen wollen.
Wir wünschen uns beidseitig bedruckte Flyer auf hochwertigem Material (Chromosulfatpapier, 450 g/m²). Bei der Auswahl des Formates wollen wir euch freie Hand lassen.
Vorderseite:
- Logo von KORVEN Immobilien.
- Ein Foto als Eye-Catcher, das Interesse weckt, zum Schmunzeln bringt und in Erinnerung bleibt. Wichtig: Auf dem Foto sollte man Freude sehen (gerne lächelnde Gesichter, die Personen müssen nicht zwangsläufig in die Kamera blicken. Eine positive und glückliche Grundstimmung auf dem Bild ist wichtig). -> an dieser Stelle bitte geeignete Stock-Bilder recherchieren und diese vorschlagen.
- Claim: Genießen Sie Ihre Freiheit. Wir verkaufen Ihre Immobilie.
Rückseite:
folgenden Text bitte verwenden:
Das Besondere bei KORVEN Immobilien:
- langjährige Erfahrung mit Immobilien des gehobenen Segments
- hochprofessionelle Komplettabwicklung in kürzester Zeit
- ausgezeichnete Referenzen
- auf Wunsch sehr diskrete Abwicklung
Anschließend bitte einen Satz, der eine Abschlussfrage formuliert, die etwa folgenden Inhalt wiedergibt:
'Wenn Sie direkt mit uns sprechen möchten, erreichen Sie uns jederzeit unter 0157 - 3948 2036.'
(Diesen Satz könnt ihr gerne umformulieren.)
Website und Emailadresse [ www.korven-immobilien.example - ib@korven-immobilien.example ]
Bilder des gesamten KORVEN Verkaufsteam als Einzelportraits vor dunklem Hintergrund.
Dabei wichtig: Lorenz Korven als Chef bitte an die erste Stelle setzen. Henrike und Jonas Weidlich sind ein Ehepaar, die Immobilien meist gemeinsam verkaufen, daher bitte auch ihre beiden Portraits nebeneinander platzieren.
Bei der Gestaltung des Flyers i..

```html
<!DOCTYPE html>
<html lang="de">
<head>
<meta charset="utf-8">
<title>KORVEN Immobilien – Flyer</title>
<link href="https://fonts.googleapis.com/css2?family=Cinzel:wght@400;600&family=Montserrat:wght@500;700;800&family=Didact+Gothic&display=swap" rel="stylesheet">
<style>
  :root{
    --navy:#1b2462;
    --gold:#a88a5a;
    --gold-light:#c2a574;
    --ink:#1b2462;
    --light:#e6e8ec;
    --dark:#17171c;
    --white:#ffffff;
    --page:#ffffff;
  }
  *{box-sizing:border-box;margin:0;padding:0}
  html,body{width:1200px;height:837px;overflow:hidden;background:var(--page)}
  .canvas{position:relative;width:1200px;height:837px}
  .flyer{position:absolute;top:138px;width:560px;height:560px;overflow:hidden;box-shadow:0 6px 24px rgba(0,0,0,.18)}
  .flyer--front{left:26px}
  .flyer--back{left:614px}

  /* front */
  .front-photo{position:absolute;inset:0 0 150px 0;
    background:radial-gradient(circle at 20% 80%,#f3a53a 0%,#c9782f 18%,transparent 45%),
               linear-gradient(160deg,#e9e2dc 0%,#c9b8aa 40%,#8d6d58 70%,#5b4a3c 100%)}
  .front-band{position:absolute;left:0;right:0;bottom:0;height:190px;background:var(--navy);
    clip-path:polygon(0 22%,100% 0,100% 100%,0 100%)}
  .front-stripe{position:absolute;left:0;right:0;bottom:0;height:196px;background:var(--gold);
    clip-path:polygon(0 21%,100% 0,100% 3%,0 24%)}
  .logo-box{position:absolute;left:0;top:36px;width:180px;height:100px;background:var(--white);
    display:flex;flex-direction:column;align-items:center;justify-content:center}
  .wordmark{font-family:'Cinzel',serif;font-weight:600;color:var(--navy);font-size:30px;letter-spacing:4px;line-height:1}
  .wordmark-sub{font-family:'Cinzel',serif;font-weight:400;color:var(--navy);font-size:9px;letter-spacing:6px;margin-top:6px;border-top:1px solid var(--navy);padding-top:4px}
  .claim{position:absolute;left:30px;bottom:36px;font-family:'Cinzel',serif;font-weight:600;font-size:27px;line-height:1.35;color:var(--white);letter-spacing:1px}
  .claim .accent{color:var(--gold-light)}

  /* back */
  .back-photo{position:absolute;left:0;right:0;top:0;height:210px;
    background:linear-gradient(180deg,#7fb0d9 0%,#a9cdb0 30%,#4f8a3e 65%,#2e5a26 100%)}
  .back-navy{position:absolute;left:0;right:0;top:160px;height:222px;background:var(--navy);
    clip-path:polygon(0 22%,100% 0,100% 100%,0 100%)}
  .back-stripe{position:absolute;left:0;right:0;top:156px;height:60px;background:var(--gold);
    clip-path:polygon(0 88%,100% 6%,100% 12%,0 94%)}
  .badge{position:absolute;right:22px;top:96px;width:104px;height:104px;border-radius:50%;
    background:var(--navy);border:4px solid var(--white);box-shadow:0 3px 10px rgba(0,0,0,.3);
    display:flex;flex-direction:column;align-items:center;justify-content:center;
    font-family:'Montserrat',sans-serif;font-weight:800;font-size:9.5px;line-height:1.25;text-align:center}
  .badge .w{color:var(--white)}
  .badge .g{color:var(--gold-light)}
  .usp{position:absolute;left:34px;top:224px;color:var(--white)}
  .usp-title{font-family:'Cinzel',serif;font-weight:600;font-size:17px;letter-spacing:.5px;margin-bottom:8px}
  .usp-title .accent{color:var(--gold-light)}
  .usp-list{list-style:none;font-family:'Didact Gothic',sans-serif;font-size:12.5px;line-height:1.75}
  .usp-list li{display:flex;align-items:center;gap:9px}
  .usp-list svg{flex:none}

  .contact-panel{position:absolute;left:0;right:0;top:382px;height:66px;background:var(--light)}
  .contact-panel .brand{position:absolute;left:22px;top:12px;display:flex;flex-direction:column;align-items:center}
  .contact-panel .wordmark{font-size:22px;letter-spacing:3px}
  .contact-panel .wordmark-sub{font-size:7px;letter-spacing:5px}
  .contact{position:absolute;left:178px;right:14px;top:10px;font-family:'Montserrat',sans-serif;color:var(--ink)}
  .contact-lead{font-size:8px;font-weight:500;white-space:nowrap}
  .contact-row{display:flex;align-items:center;justify-content:space-between;margin-top:5px}
  .phone{display:flex;align-items:center;gap:6px;font-weight:800;font-size:19px;white-space:nowrap;line-height:1}
  .links{font-size:8px;font-weight:500;line-height:1.7;white-space:nowrap}
  .links span{display:flex;align-items:center;gap:5px}

  .team{position:absolute;left:0;right:0;top:448px;bottom:0;background:var(--dark)}
  .team-title{position:absolute;right:18px;top:7px;font-family:'Cinzel',serif;font-weight:600;font-size:13px;color:var(--white);letter-spacing:.5px;line-height:1}
  .team-title .accent{color:var(--gold-light)}
  .team-grid{position:absolute;left:12px;right:12px;top:28px;display:flex;justify-content:space-between}
  .member{width:80px;display:flex;flex-direction:column;align-items:center}
  .portrait{width:74px;height:62px;border-bottom:3px solid var(--navy);
    background:radial-gradient(circle at 50% 40%,#5a4a42 0%,#2c2a2e 55%,#1d1d22 100%)}
  .name{font-family:'Montserrat',sans-serif;font-weight:700;font-size:7px;color:var(--white);margin-top:4px;white-space:nowrap;text-align:center}
</style>
</head>
<body>
<main class="canvas">

  <section class="flyer flyer--front" aria-label="Vorderseite">
    <div class="front-photo" role="img" aria-label="Foto: glückliches Paar umarmt sich vor einer modernen Villa im Abendlicht"></div>
    <div class="front-stripe"></div>
    <div class="front-band"></div>
    <div class="logo-box">
      <span class="wordmark">KORVEN</span>
      <span class="wordmark-sub">IMMOBILIEN</span>
    </div>
    <h1 class="claim">
      <span class="accent">Geniessen</span> Sie Ihre Freiheit.<br>
      Wir verkaufen <span class="accent">Ihre Immobilie.</span>
    </h1>
  </section>

  <section class="flyer flyer--back" aria-label="Rückseite">
    <div class="back-photo" role="img" aria-label="Foto: moderner weißer Bungalow mit Terrasse im Grünen"></div>
    <div class="back-stripe"></div>
    <div class="back-navy"></div>
    <div class="badge"><span class="w">KOSTENLOSE</span><span class="g">IMMOBILIEN</span><span class="g">BEWERTUNG</span></div>

    <div class="usp">
      <h2 class="usp-title">Das Besondere bei <span class="accent">KORVEN Immobilien</span></h2>
      <ul class="usp-list">
        <li><svg width="12" height="12" viewBox="0 0 12 12"><path d="M1 6l3.5 3.5L11 2" stroke="#fff" stroke-width="2" fill="none"/></svg>langjährige Erfahrung mit Immobilien des gehobenen Segments</li>
        <li><svg width="12" height="12" viewBox="0 0 12 12"><path d="M1 6l3.5 3.5L11 2" stroke="#fff" stroke-width="2" fill="none"/></svg>hochprofessionelle Komplettabwicklung in kürzester Zeit</li>
        <li><svg width="12" height="12" viewBox="0 0 12 12"><path d="M1 6l3.5 3.5L11 2" stroke="#fff" stroke-width="2" fill="none"/></svg>ausgezeichnete Referenzen</li>
        <li><svg width="12" height="12" viewBox="0 0 12 12"><path d="M1 6l3.5 3.5L11 2" stroke="#fff" stroke-width="2" fill="none"/></svg>auf Wunsch sehr diskrete Abwicklung</li>
      </ul>
    </div>

    <div class="contact-panel">
      <div class="brand">
        <span class="wordmark">KORVEN</span>
        <span class="wordmark-sub">IMMOBILIEN</span>
      </div>
      <div class="contact">
        <p class="contact-lead">Wenn Sie direkt mit uns sprechen möchten, erreichen Sie uns jederzeit unter:</p>
        <div class="contact-row">
          <span class="phone">
            <svg width="16" height="16" viewBox="0 0 24 24"><path d="M6.6 10.8a15 15 0 006.6 6.6l2.2-2.2c.3-.3.7-.4 1-.2 1.1.4 2.3.6 3.6.6.6 0 1 .4 1 1V20c0 .6-.4 1-1 1A17 17 0 013 4c0-.6.4-1 1-1h3.5c.6 0 1 .4 1 1 0 1.3.2 2.5.6 3.6.1.3 0 .7-.2 1z" fill="var(--ink)"/></svg>
            0157 - 3948 2036
          </span>
          <span class="links">
            <span><svg width="10" height="8" viewBox="0 0 10 8"><rect width="10" height="8" fill="var(--ink)"/><path d="M0 0l5 4 5-4" stroke="#fff" fill="none"/></svg>ib@korven-immobilien.example</span>
            <span><svg width="10" height="10" viewBox="0 0 10 10"><circle cx="5" cy="5" r="4.3" stroke="var(--ink)" fill="none"/><path d="M.7 5h8.6M5 .7c-2 2.5-2 6.1 0 8.6M5 .7c2 2.5 2 6.1 0 8.6" stroke="var(--ink)" fill="none" stroke-width=".8"/></svg>www.korven-immobilien.example</span>
          </span>
        </div>
      </div>
    </div>

    <div class="team">
      <h2 class="team-title">Unser <span class="accent">Team</span></h2>
      <div class="team-grid">
        <figure class="member"><div class="portrait" role="img" aria-label="Portrait von Lorenz A. Korven vor dunklem Hintergrund"></div><figcaption class="name">Lorenz A. Korven</figcaption></figure>
        <figure class="member"><div class="portrait" role="img" aria-label="Portrait von Henrike Weidlich vor dunklem Hintergrund"></div><figcaption class="name">Henrike Weidlich</figcaption></figure>
        <figure class="member"><div class="portrait" role="img" aria-label="Portrait von Jonas Weidlich vor dunklem Hintergrund"></div><figcaption class="name">Jonas Weidlich</figcaption></figure>
        <figure class="member"><div class="portrait" role="img" aria-label="Portrait von Greta Holmsted vor dunklem Hintergrund"></div><figcaption class="name">Greta Holmsted</figcaption></figure>
        <figure class="member"><div class="portrait" role="img" aria-label="Portrait von Dr. Ilse Brandvoort vor dunklem Hintergrund"></div><figcaption class="name">Dr. Ilse Brandvoort</figcaption></figure>
        <figure class="member"><div class="portrait" role="img" aria-label="Portrait von Mira Lenhart vor dunklem Hintergrund"></div><figcaption class="name">Mira Lenhart</figcaption></figure>
      </div>
    </div>
  </section>

</main>
</body>
</html>
```